Hello , we need a 1 page A4 flyer. the flyer needs a heading and then 4 sub headings and catagoring. The words on the attached example are the same length as our text. we are open to a new modern look and the information can be in 1 or 2 coloums. we are an australian law firm and I have also attachd our logo. the bottom 1/4 of the page is a graphic you need to allow space for. we have blue as a corporate colour and do not have a font or style. please use the 5 headings and we will complete the words / text afterwards so we will need the final version to be a word document. for assistance see www.jurapath-example.com.au
Legal

```html
<!DOCTYPE html>
<html lang="en">
<head>
<meta charset="utf-8">
<title>JuraPath Flyer</title>
<link rel="stylesheet" href="https://fonts.googleapis.com/css2?family=Poppins:wght@400;500;700&display=swap">
<style>
  :root {
    --page-bg: #ffffff;
    --sheet: #ffffff;
    --navy: #0c3466;
    --brand-blue: #1e9ad6;
    --light-blue: #5ec3f2;
    --body-text: #4a4f57;
  }
  * { box-sizing: border-box; margin: 0; padding: 0; }
  html, body {
    width: 1200px; height: 2989px; overflow: hidden;
    background: var(--page-bg);
    font-family: "Poppins", Arial, sans-serif;
  }
  .flyer {
    position: absolute; left: 80px; top: 758px;
    width: 826px; height: 1170px;
    background: var(--sheet);
    transform: scale(1.259); transform-origin: 0 0;
    box-shadow: 0 2px 10px rgba(0,0,0,0.18);
    overflow: hidden;
  }
  .brand-name {
    position: absolute; left: 62px; top: 112px;
    font-size: 32px; font-weight: 500;
    color: var(--navy); letter-spacing: 0.3px; line-height: 1;
  }
  .hero-photo { position: absolute; left: 0; top: 0; }
  .intro-band {
    position: absolute; left: 60px; top: 360px; width: 723px; height: 97px;
    background: var(--navy); color: #fff; text-align: center; padding-top: 6px;
  }
  .intro-title { font-size: 38px; font-weight: 700; line-height: 1.15; letter-spacing: 0.3px; }
  .intro-title span { color: var(--light-blue); }
  .intro-text { font-size: 12.4px; line-height: 1.45; padding: 3px 8px 0; }
  .feature { position: absolute; width: 300px; }
  .feature-icon {
    position: absolute; left: -57px; top: 3px; width: 43px; height: 38px;
  }
  .feature-title {
    font-size: 15.8px; font-weight: 700; color: var(--navy);
    line-height: 1.22; text-transform: uppercase;
  }
  .feature-text { font-size: 10.9px; color: var(--body-text); line-height: 1.18; margin-top: 8px; }
  .feature-text + .feature-text { margin-top: 11px; }
  .f1 { left: 117px; top: 482px; }
  .f2 { left: 489px; top: 482px; }
  .f3 { left: 117px; top: 670px; }
  .f4 { left: 489px; top: 670px; }
  .skyline-band { position: absolute; left: 0; top: 852px; }
  .web-tab { position: absolute; left: 0; top: 1118px; width: 826px; height: 52px; }
  .web-address {
    position: absolute; left: 0; top: 1124px; width: 826px; text-align: center;
    font-size: 19px; color: #fff; letter-spacing: 0.3px;
  }
  .web-address b { font-weight: 500; }
</style>
</head>
<body>
  <main class="flyer">
    <svg class="hero-photo" width="826" height="460" viewBox="0 0 826 460" role="img" aria-label="Photograph of a harbour city skyline at dusk">
      <defs>
        <linearGradient id="heroTone" x1="0" y1="0" x2="0" y2="1">
          <stop offset="0" stop-color="#2f95dd"/>
          <stop offset="0.35" stop-color="#4d7fa8"/>
          <stop offset="0.7" stop-color="#6a5a4c"/>
          <stop offset="1" stop-color="#2c3c52"/>
        </linearGradient>
      </defs>
      <polygon points="357,46 783,46 783,360 60,360 60,190 275,190" fill="url(#heroTone)"/>
    </svg>

    <div class="brand-name">JuraPath</div>

    <section class="intro-band">
      <h1 class="intro-title">WHO IS <span>JURAPATH?</span></h1>
      <p class="intro-text">This is a statement header small paragraph. This is a statement header small paragraph. This is a statement<br>header small paragraph. This is a statement header small paragraph</p>
    </section>

    <article class="feature f1">
      <svg class="feature-icon" viewBox="0 0 43 38" aria-hidden="true">
        <rect width="43" height="38" fill="#1e9ad6"/>
        <circle cx="22" cy="15" r="7" fill="none" stroke="#fff" stroke-width="2"/>
        <path d="M20 12h4M20 18h4M22 10v10" stroke="#fff" stroke-width="1.5"/>
        <path d="M8 29h8l5 -3h10" stroke="#fff" stroke-width="2.2" fill="none"/>
      </svg>
      <h2 class="feature-title">Next generation legal<br>and lender process services</h2>
      <p class="feature-text">Paragraph 1. Paragraph 1. Paragraph 1. Paragraph 1. Paragraph 1. Paragraph 1. Paragraph 1. Paragraph 1. Paragraph 1. Paragraph 1. Paragraph 1. Paragraph 1. Paragraph 1. Paragraph 1. Paragraph 1. Paragraph 1.</p>
      <p class="feature-text">Paragraph 2. Paragraph 2. Paragraph 2. Paragraph 2. Paragraph 2. Paragraph 2. Paragraph 2. Paragraph 2. Paragraph 2. Paragraph 2. Paragraph 2. Paragraph 2. Paragraph 2. Paragraph 2. Paragraph 2. Paragraph 2. Paragraph 2. Paragraph 2.</p>
    </article>

    <article class="feature f2">
      <svg class="feature-icon" viewBox="0 0 43 38" aria-hidden="true">
        <rect width="43" height="38" fill="#1e9ad6"/>
        <circle cx="14" cy="17" r="6" fill="none" stroke="#fff" stroke-width="2"/>
        <rect x="20" y="20" width="16" height="9" fill="none" stroke="#fff" stroke-width="2"/>
        <path d="M8 31h28" stroke="#fff" stroke-width="2"/>
        <circle cx="30" cy="11" r="3" fill="#fff"/>
      </svg>
      <h2 class="feature-title">We understand the importance<br>of the work we do for you</h2>
      <p class="feature-text">Paragraph 1. Paragraph 1. Paragraph 1. Paragraph 1. Paragraph 1. Paragraph 1. Paragraph 1. Paragraph 1. Paragraph 1. Paragraph 1. Paragraph 1. Paragraph 1. Paragraph 1. Paragraph 1. Paragraph 1. Paragraph 1. Paragraph 1. Paragraph 1.</p>
      <p class="feature-text">Paragraph 2. Paragraph 2. Paragraph 2. Paragraph 2. Paragraph 2. Paragraph 2. Paragraph 2. Paragraph 2. Paragraph 2. Paragraph 2. Paragraph 2. Paragraph 2.</p>
    </article>

    <article class="feature f3">
      <svg class="feature-icon" viewBox="0 0 43 38" aria-hidden="true">
        <rect width="43" height="38" fill="#1e9ad6"/>
        <circle cx="14" cy="19" r="7" fill="none" stroke="#fff" stroke-width="2"/>
        <rect x="23" y="20" width="3" height="9" fill="#fff"/>
        <rect x="28" y="15" width="3" height="14" fill="#fff"/>
        <rect x="33" y="10" width="3" height="19" fill="#fff"/>
      </svg>
      <h2 class="feature-title">How you will benefit from us</h2>
      <p class="feature-text">Paragraph 1. Paragraph 1. Paragraph 1. Paragraph 1. Paragraph 1. Paragraph 1. Paragraph 1. Paragraph 1. Paragraph 1. Paragraph 1. Paragraph 1. Paragraph 1. Paragraph 1. Paragraph 1. Paragraph 1. Paragraph 1. Paragraph 1. Paragraph 1. Paragraph 1. Paragraph 1. Paragraph 1. Paragraph 1. Paragraph 1. Paragraph 1. Paragraph 1. Paragraph 1. Paragraph 1. Paragraph 1. Paragraph 1. Paragraph 1. Paragraph 1. Paragraph 1. Paragraph 1. Paragraph 1.</p>
    </article>

    <article class="feature f4">
      <svg class="feature-icon" viewBox="0 0 43 38" aria-hidden="true">
        <rect width="43" height="38" fill="#1e9ad6"/>
        <path d="M8 14l8 -6 6 5 6 -5 8 6 -10 14 -8 -4z" fill="none" stroke="#fff" stroke-width="2" stroke-linejoin="round"/>
      </svg>
      <h2 class="feature-title">Results, not just promises</h2>
      <p class="feature-text">Paragraph 1. Paragraph 1. Paragraph 1. Paragraph 1. Paragraph 1. Paragraph 1. Paragraph 1. Paragraph 1. Paragraph 1. Paragraph 1. Paragraph 1</p>
      <p class="feature-text">Paragraph 2. Paragraph 2. Paragraph 2. Paragraph 2. Paragraph 2. Paragraph 2. Paragraph 2. Paragraph 2.</p>
    </article>

    <svg class="skyline-band" width="826" height="318" viewBox="0 0 826 318" role="img" aria-label="Faint grey city skyline graphic">
      <defs>
        <linearGradient id="skylineTone" x1="0" y1="0" x2="0" y2="1">
          <stop offset="0" stop-color="#efefef"/>
          <stop offset="1" stop-color="#e3e3e3"/>
        </linearGradient>
      </defs>
      <rect width="826" height="318" fill="url(#skylineTone)"/>
    </svg>

    <svg class="web-tab" width="826" height="52" viewBox="0 0 826 52" aria-hidden="true">
      <polygon points="250,0 577,0 597,44 230,44" fill="#1e9ad6"/>
      <rect x="0" y="44" width="826" height="8" fill="#1e9ad6"/>
    </svg>
    <p class="web-address">www.<b>jurapath-example</b>.com.au</p>
  </main>
</body>
</html>
```